依頼詳細
12月下旬~1月上旬オープンに向けてのチラシ作成をお願いいたします。オープン以降も同じチラシを定期的にポスティングいたしますので汎用できるようにお願いいたします。
納品はaiデータでお願いいたします。
記載項目
社名や電話番号は後で投稿させていただきます。
サイズ
A4
ページ数
片面
希望イメージ
シンプル 複雑
単色 カラフル
暗い 明るい
日常 高級
遊び心 厳粛
未来的 伝統的
女性的 男性的
希望する色
水色系
納品ファイル
• イラストレーター形式 (.ai)
補足説明
脱毛サロンのロゴを貼り付けさせていただきます。
脱毛器の画像や使用イメージ画像を追加させていただきます。
よろしくお願いいたします。
作成していただいているところに追記すみません。
オープン期間限定キャンペーン→その後、通常価格に戻します。
メニュー内容につきましては
30分→通常3500円
60分→通常4500円
月額会員→通常5500円(初月のみ)
全メニュー1000円off!!
ずーっと会員登録費・事務手数料【無料】
■ 選んだ理由

わかりやすさ。色合い

■ 提案者全員のお礼・コメント

今回たくさんのご応募いただきありがとうございます。
また、どの提案も素敵なもので決めるのに苦慮しました。またよろしくお願いいたします。

```html
<!DOCTYPE html>
<html lang="ja">
<head>
<meta charset="utf-8">
<title>sorano セルフ脱毛サロン</title>
<link rel="stylesheet" href="https://fonts.googleapis.com/css2?family=M+PLUS+Rounded+1c:wght@400;700;800&family=Noto+Sans+JP:wght@400;700;900&family=Cormorant+Garamond:wght@500&display=swap">
<style>
:root{
  --sky:#7ccbe8;
  --sky-deep:#2f9fd2;
  --sky-pale:#e6f5fb;
  --navy:#1f3f6e;
  --orange:#f28a2a;
  --pink:#f08a9c;
  --pink-deep:#e4566f;
  --pink-pale:#fde4e8;
  --text:#4a4a4a;
  --white:#ffffff;
}
*{box-sizing:border-box;margin:0;padding:0}
html,body{width:848px;height:1200px;overflow:hidden}
body{font-family:"Noto Sans JP",sans-serif;color:var(--text);background:var(--white)}
.flyer{position:relative;width:848px;height:1200px;overflow:hidden;
  background:linear-gradient(180deg,#f6fafc 0%,#eef7fb 45%,#d6eef8 72%,#bde4f4 100%)}
.hero-photo{position:absolute;left:0;top:0;width:848px;height:600px;
  background:
    radial-gradient(ellipse 420px 260px at 330px 250px,rgba(240,205,185,.95) 0%,rgba(240,205,185,0) 70%),
    radial-gradient(ellipse 360px 200px at 560px 360px,rgba(236,196,176,.85) 0%,rgba(236,196,176,0) 70%),
    radial-gradient(ellipse 300px 220px at 150px 120px,rgba(250,228,214,.9) 0%,rgba(250,228,214,0) 70%),
    linear-gradient(165deg,#dfe6ec 0%,#eee3dc 35%,#f3e6de 55%,#e5edf2 80%,#eef7fb 100%);
  -webkit-mask-image:linear-gradient(180deg,#000 70%,transparent 100%);
  mask-image:linear-gradient(180deg,#000 70%,transparent 100%)}
.brand{position:absolute;left:620px;top:50px;width:180px;text-align:center;color:var(--sky-deep)}
.brand-dot{width:30px;height:30px;border-radius:50%;background:var(--sky);margin:0 auto 8px}
.brand-name{font-family:"Cormorant Garamond",serif;font-size:62px;line-height:1;letter-spacing:2px}
.brand-kana{font-size:16px;letter-spacing:6px;margin-top:6px}
.open-badge{position:absolute;left:628px;top:362px;width:130px;height:130px;border-radius:50%;
  background:var(--sky-deep);color:var(--white);text-align:center;padding-top:22px;
  font-family:"M PLUS Rounded 1c",sans-serif;font-weight:800;box-shadow:0 0 0 4px rgba(255,255,255,.7)}
.open-badge .year{font-size:20px;line-height:1.2}
.open-badge .date{display:inline-block;background:var(--white);color:var(--orange);font-size:22px;line-height:1.3;padding:0 8px;border-radius:4px;margin:3px 0}
.open-badge .open{font-size:22px;letter-spacing:1px;line-height:1.2}
.headline{position:absolute;left:52px;top:418px;font-family:"M PLUS Rounded 1c",sans-serif;font-weight:800;white-space:nowrap}
.headline .sub{font-size:58px;color:var(--sky-deep);letter-spacing:2px;line-height:1.2}
.headline .sub em{font-style:normal;font-size:44px}
.headline .main{font-size:88px;color:var(--orange);letter-spacing:3px;line-height:1.15}
.features{position:absolute;left:40px;top:572px;width:768px;display:flex;justify-content:space-between}
.feature{width:240px;text-align:center}
.feature-photo{width:160px;height:160px;border-radius:50%;margin:0 auto;border:5px solid var(--white);box-shadow:0 2px 8px rgba(47,159,210,.15)}
.feature:nth-child(1) .feature-photo{background:radial-gradient(circle at 55% 40%,#f3d9c8 0%,#e7eef2 45%,#9fd3ea 100%)}
.feature:nth-child(2) .feature-photo{background:radial-gradient(circle at 50% 45%,#f1cdb5 0%,#f5e2d4 50%,#e9d6c8 100%)}
.feature:nth-child(3) .feature-photo{background:radial-gradient(circle at 50% 40%,#f2d2c0 0%,#f6dde3 50%,#eeb4c0 100%)}
.feature-label{display:inline-block;margin-top:-16px;position:relative;background:var(--orange);color:var(--white);
  font-family:"M PLUS Rounded 1c",sans-serif;font-weight:800;font-size:22px;padding:4px 18px;border-radius:22px}
.feature:nth-child(1) .feature-label{background:var(--sky-deep)}
.feature:nth-child(3) .feature-label{background:var(--pink)}
.feature-text{font-size:13px;line-height:1.6;margin-top:8px;color:var(--text)}
.safety{position:absolute;left:0;top:892px;width:848px;text-align:center;color:var(--orange);font-weight:700;font-size:21px}
.safety::before,.safety::after{content:"";display:inline-block;width:14px;height:2px;background:var(--orange);vertical-align:middle;margin:0 10px}
.courses{position:absolute;left:52px;top:934px;width:744px;display:flex;justify-content:space-between}
.course{width:360px;height:118px;border-radius:10px;background:var(--pink-pale);overflow:hidden;text-align:center}
.course-title{background:var(--pink);color:var(--white);font-weight:700;font-size:22px;padding:5px 0;letter-spacing:1px}
.course-price{color:var(--pink-deep);font-family:"M PLUS Rounded 1c",sans-serif;font-weight:800;padding-top:6px;white-space:nowrap}
.course-price .time{font-size:32px;margin-right:12px}
.course-price .yen{font-size:50px}
.footer{position:absolute;left:0;top:1074px;width:848px;height:126px;
  background:linear-gradient(90deg,#e9f6fb 0%,#cdeaf6 100%);display:flex;align-items:center;padding:0 40px}
.footer-brand{display:flex;align-items:center;gap:10px;color:var(--sky-deep)}
.footer-brand .dot{width:18px;height:18px;border-radius:50%;background:var(--sky)}
.footer-brand .name{font-family:"Cormorant Garamond",serif;font-size:44px;line-height:1}
.footer-brand .kana{font-size:16px}
.contact{margin-left:36px;color:var(--navy)}
.contact .tel{font-size:34px;font-weight:900;letter-spacing:1px;display:flex;align-items:baseline;gap:6px;line-height:1.2}
.contact .tel small{font-size:18px}
.contact .addr{font-size:12px;margin-top:2px}
.map{margin-left:auto;width:180px;height:90px;background:var(--white);border:1px solid #cfd8dd;display:flex;align-items:center;justify-content:center;font-size:12px;color:#7a8a94}
</style>
</head>
<body>
<div class="flyer">
  <div class="hero-photo" role="img" aria-label="素肌の脚にそっと手を添える女性のイメージ写真"></div>

  <div class="brand">
    <div class="brand-dot"></div>
    <div class="brand-name">sorano</div>
    <div class="brand-kana">-そらの-</div>
  </div>

  <div class="open-badge">
    <div class="year">2022年</div>
    <div class="date">1月上旬</div>
    <div class="open">OPEN</div>
  </div>

  <div class="headline">
    <div class="sub">低価格<em>で</em>お手軽</div>
    <div class="main">セルフ脱毛サロン</div>
  </div>

  <div class="features">
    <div class="feature">
      <div class="feature-photo" role="img" aria-label="脱毛器を手に持つスタッフのイメージ写真"></div>
      <div class="feature-label">リーズナブルに</div>
      <p class="feature-text">人件費を最小限に抑えることで、<br>価格に反映しています。</p>
    </div>
    <div class="feature">
      <div class="feature-photo" role="img" aria-label="腕を上げたわきのイメージ写真"></div>
      <div class="feature-label">お好きな箇所を</div>
      <p class="feature-text">人の目を気にせず希望の箇所を<br>自分のペースで処理できます。</p>
    </div>
    <div class="feature">
      <div class="feature-photo" role="img" aria-label="笑顔の女性スタッフのイメージ写真"></div>
      <div class="feature-label">初めてでも安心</div>
      <p class="feature-text">マシン操作はとても簡単！<br>スタッフ常駐なので安心です。</p>
    </div>
  </div>

  <p class="safety">お子さまにもご利用いただける安心安全の機材です</p>

  <div class="courses">
    <div class="course">
      <div class="course-title">ポイント脱毛コース</div>
      <div class="course-price"><span class="time">30分</span><span class="yen">¥0,000</span></div>
    </div>
    <div class="course">
      <div class="course-title">全身脱毛コース</div>
      <div class="course-price"><span class="time">60分</span><span class="yen">¥0,000</span></div>
    </div>
  </div>

  <div class="footer">
    <div class="footer-brand">
      <span class="dot"></span>
      <span class="name">sorano</span>
      <span class="kana">そらの</span>
    </div>
    <div class="contact">
      <div class="tel"><small>TEL.</small>0000-00-0000</div>
      <div class="addr">〒000-0000 ○○県○○市○○000-0</div>
    </div>
    <div class="map">MAP</div>
  </div>
</div>
</body>
</html>
```